Ferris Contracting LLC Business Card Design

I am looking for a creative and unique business card design. We are a commercial construction general contractor. With the name "FERRIS" Contracting, I am hoping to see some neat designs that correlate with the name.

```html
<!DOCTYPE html>
<html lang="fr">
<head>
<meta charset="utf-8">
<title>Ferris Contracting LLC – Business Card</title>
<link rel="stylesheet" href="https://fonts.googleapis.com/css2?family=Lato:wght@400;700;900&display=swap">
<style>
  :root {
    --backdrop: #808080;
    --card-black: #000000;
    --frame-silver-light: #f2f2f2;
    --frame-silver-dark: #9a9a9a;
    --brand-blue: #1f8fd6;
    --brand-blue-light: #3aa9ea;
    --brand-blue-dark: #0b63a8;
    --text-white: #ffffff;
  }
  * { margin: 0; padding: 0; box-sizing: border-box; }
  html, body {
    width: 1200px; height: 506px; overflow: hidden;
    background: var(--backdrop);
    font-family: "Lato", Arial, sans-serif;
  }
  .canvas { position: relative; width: 1200px; height: 506px; }

  .card {
    position: absolute; top: 115px; width: 480px; height: 275px;
    padding: 4px;
    background: linear-gradient(135deg, var(--frame-silver-dark), var(--frame-silver-light) 40%, var(--frame-silver-dark) 70%, var(--frame-silver-light));
    box-shadow: 0 2px 6px rgba(0,0,0,.35);
  }
  .card-front { left: 100px; }
  .card-back { left: 620px; }
  .card-face { position: relative; width: 100%; height: 100%; background: var(--card-black); overflow: hidden; }

  /* front */
  .brand-name {
    position: absolute; color: var(--brand-blue);
    font-weight: 900; text-transform: uppercase; line-height: 1;
  }
  .card-front .brand-name { left: 26px; top: 98px; font-size: 30px; letter-spacing: 1px; }
  .card-front .brand-name small { display: block; font-size: 12.5px; letter-spacing: 5.4px; margin-top: 4px; }
  .brand-dot {
    position: absolute; left: 18px; top: 76px; width: 14px; height: 14px;
    border-radius: 50%; background: var(--brand-blue);
  }

  .holder { position: absolute; right: 34px; top: 56px; text-align: right; }
  .holder-name { color: var(--brand-blue); font-weight: 700; font-size: 15px; }
  .holder-title {
    color: var(--brand-blue); font-size: 11px; padding-bottom: 6px; margin-top: 2px;
    border-bottom: 1px solid var(--brand-blue); display: inline-block; width: 72px;
  }

  .contact-list { position: absolute; right: 34px; top: 117px; list-style: none; }
  .contact-item {
    display: flex; justify-content: flex-end; align-items: center; gap: 12px;
    color: var(--text-white); font-size: 10.5px; text-align: right; line-height: 1.45;
  }
  .contact-item + .contact-item { margin-top: 7px; }
  .contact-address { margin-bottom: 5px; }
  .contact-icon {
    flex: none; width: 13px; height: 13px; background: var(--brand-blue);
    display: flex; align-items: center; justify-content: center;
  }

  .bottom-band { position: absolute; left: 12px; bottom: 5px; width: 450px; height: 19px; }

  /* back */
  .side-tab { position: absolute; top: 0; left: 0; }
  .card-back .brand-name { left: 0; right: 0; top: 98px; text-align: center; font-size: 60px; letter-spacing: 2px; }
  .card-back .brand-name small { display: block; font-size: 22px; letter-spacing: 9px; margin-top: 6px; }
</style>
</head>
<body>
<main class="canvas">

  <section class="card card-front" aria-label="Card front">
    <div class="card-face">
      <span class="brand-dot"></span>
      <div class="brand-name">Ferris<small>Contracting</small></div>

      <div class="holder">
        <div class="holder-name">MARC DELORME</div>
        <div class="holder-title">Président</div>
      </div>

      <ul class="contact-list">
        <li class="contact-item contact-address">
          <span>2480 rue des Érables, Saint-Augustin,<br>Québec, G3A 1B7</span>
          <span class="contact-icon"><svg width="8" height="10" viewBox="0 0 8 10"><path d="M4 0a3.5 3.5 0 0 0-3.5 3.5C.5 6 4 10 4 10s3.5-4 3.5-6.5A3.5 3.5 0 0 0 4 0z" fill="#000"/><circle cx="4" cy="3.5" r="1.3" fill="#1f8fd6"/></svg></span>
        </li>
        <li class="contact-item">
          <span>000000000000</span>
          <span class="contact-icon"><svg width="9" height="9" viewBox="0 0 10 10"><path d="M2 0l2 2.5-1.2 1.3a6 6 0 0 0 3.4 3.4L7.5 6 10 8l-1.5 2C4 10 0 6 0 1.5z" fill="#000"/></svg></span>
        </li>
        <li class="contact-item">
          <span>ferris*********@mailbox.com</span>
          <span class="contact-icon"><svg width="9" height="7" viewBox="0 0 9 7"><rect x=".5" y=".5" width="8" height="6" fill="none" stroke="#000"/><path d="M.5.5l4 3.5 4-3.5" fill="none" stroke="#000"/></svg></span>
        </li>
        <li class="contact-item">
          <span>www.ferrisbuild.com</span>
          <span class="contact-icon"><svg width="8" height="9" viewBox="0 0 8 9"><path d="M1 0v8l2-2 1.5 3 1.3-.6L4.3 5.4H7z" fill="#000"/></svg></span>
        </li>
      </ul>

      <svg class="bottom-band" viewBox="0 0 450 19" aria-hidden="true">
        <defs>
          <linearGradient id="bandSilver" x1="0" x2="1">
            <stop offset="0" stop-color="#8f8f8f"/><stop offset=".5" stop-color="#ffffff"/><stop offset="1" stop-color="#9c9c9c"/>
          </linearGradient>
          <linearGradient id="bandBlue" x1="0" x2="1">
            <stop offset="0" stop-color="#0b63a8"/><stop offset=".45" stop-color="#3aa9ea"/><stop offset="1" stop-color="#0b63a8"/>
          </linearGradient>
        </defs>
        <polygon points="0,0 234,0 218,19 0,19" fill="url(#bandSilver)"/>
        <polygon points="240,0 450,0 450,19 224,19" fill="url(#bandBlue)"/>
      </svg>
    </div>
  </section>

  <section class="card card-back" aria-label="Card back">
    <div class="card-face">
      <svg class="side-tab" width="472" height="267" viewBox="0 0 472 267" aria-hidden="true">
        <defs>
          <linearGradient id="tabBlue" x1="0" x2="0" y1="0" y2="1">
            <stop offset="0" stop-color="#0b63a8"/><stop offset=".5" stop-color="#3aa9ea"/><stop offset="1" stop-color="#0b63a8"/>
          </linearGradient>
        </defs>
        <polygon points="0,56 28,72 28,196 0,212" fill="url(#tabBlue)"/>
        <polygon points="472,56 444,72 444,196 472,212" fill="url(#tabBlue)"/>
      </svg>
      <div class="brand-name">Ferris<small>Contracting</small></div>
    </div>
  </section>

</main>
</body>
</html>
```